Kestrel Forge Tech
Bus. Cards/Stationary/Presentation
Kestrel Forge Tech - Information Technology
Creative Brief
Use specific fonts
Open to ideas on font pairing
Professional
Wendell Pask
Owner
218 Larkspur Avenue Suite 4400 Harlow Bend, OR 97482
Wendell.Pask@kestrelforgetech.com
www.kestrelforgetech.com
I am open to my logo displayed on the back. I am also open to ideas on the back of business card. Be creative on front and back.

```html
<!DOCTYPE html>
<html lang="en">
<head>
<meta charset="utf-8">
<title>Kestrel Forge Tech – Business Card</title>
<link rel="stylesheet" href="https://fonts.googleapis.com/css2?family=Open+Sans:wght@400;600&display=swap">
<style>
  :root {
    --backdrop: #eee6d9;
    --card: #ffffff;
    --ink: #58595b;
    --ink-soft: #4a4a4a;
    --accent: #7dc242;
    --rule: #9a9a9a;
  }
  * { margin: 0; padding: 0; box-sizing: border-box; }
  html, body { width: 1200px; height: 965px; overflow: hidden; }
  body {
    background: var(--backdrop);
    font-family: "Open Sans", Arial, sans-serif;
    position: relative;
  }
  .card {
    position: absolute;
    left: 150px; top: 226px;
    width: 900px; height: 512px;
    background: var(--card);
    border-radius: 28px;
    box-shadow: 0 8px 18px rgba(0,0,0,.18);
  }
  .card__tab {
    position: absolute;
    top: 250px; height: 196px; width: 24px;
    background: var(--accent);
  }
  .card__tab--left { left: 0; border-radius: 0 8px 8px 0; }
  .card__tab--right { right: 0; border-radius: 8px 0 0 8px; }

  .brand {
    position: absolute;
    left: 67px; top: 64px;
    display: flex; align-items: center; gap: 30px;
  }
  .brand__dot {
    width: 124px; height: 124px; border-radius: 50%;
    background: var(--ink);
  }
  .brand__name {
    font-weight: 600; font-size: 57px; color: var(--ink);
    letter-spacing: -0.5px; white-space: nowrap;
  }

  .person {
    position: absolute;
    right: 527px; top: 256px;
    text-align: right; color: var(--ink-soft);
    font-size: 20px; line-height: 29px;
    white-space: nowrap;
  }
  .person__name { color: var(--accent); font-weight: 600; font-size: 31px; line-height: 36px; }
  .person__role { margin-bottom: 10px; }

  .divider {
    position: absolute; left: 390px; top: 250px;
    width: 2px; height: 195px; background: var(--rule);
  }

  .contact {
    position: absolute; left: 428px; top: 260px;
    list-style: none; color: var(--ink-soft); font-size: 21px;
    white-space: nowrap;
  }
  .contact li { display: flex; align-items: center; height: 36.5px; }
  .contact svg { width: 22px; height: 22px; margin-right: 12px; fill: var(--accent); flex: none; }
</style>
</head>
<body>
  <article class="card">
    <span class="card__tab card__tab--left"></span>
    <span class="card__tab card__tab--right"></span>

    <header class="brand">
      <span class="brand__dot"></span>
      <span class="brand__name">Kestrel Forge Tech</span>
    </header>

    <div class="person">
      <p class="person__name">Wendell Pask</p>
      <p class="person__role">Owner</p>
      <p>218 Larkspur Avenue</p>
      <p>Suite 4400</p>
      <p>Harlow Bend, OR 97482</p>
    </div>

    <span class="divider"></span>

    <ul class="contact">
      <li>
        <svg viewBox="0 0 24 24" aria-hidden="true"><path d="M6.6 10.8a15 15 0 0 0 6.6 6.6l2.2-2.2a1 1 0 0 1 1-.25 11.4 11.4 0 0 0 3.6.57 1 1 0 0 1 1 1V20a1 1 0 0 1-1 1A17 17 0 0 1 3 4a1 1 0 0 1 1-1h3.5a1 1 0 0 1 1 1c0 1.25.2 2.45.57 3.57a1 1 0 0 1-.25 1z"/></svg>
        730.555.0148
      </li>
      <li>
        <svg viewBox="0 0 24 24" aria-hidden="true"><path d="M8 1h8a2 2 0 0 1 2 2v18a2 2 0 0 1-2 2H8a2 2 0 0 1-2-2V3a2 2 0 0 1 2-2zm0 3v13h8V4zm4 15a1.2 1.2 0 1 0 0 2.4A1.2 1.2 0 0 0 12 19z"/></svg>
        730.555.0162
      </li>
      <li>
        <svg viewBox="0 0 24 24" aria-hidden="true"><path d="M7 2h10v5H7zM4 8h16a2 2 0 0 1 2 2v7h-4v5H6v-5H2v-7a2 2 0 0 1 2-2zm4 8v4h8v-4z"/></svg>
        730.555.0177
      </li>
      <li>
        <svg viewBox="0 0 24 24" aria-hidden="true"><path d="M12 2a10 10 0 1 0 5 18.7l-1-1.7A8 8 0 1 1 20 12v1.3a1.7 1.7 0 0 1-3.4 0V7.5h-2v.9A5 5 0 1 0 15.4 16a3.7 3.7 0 0 0 6.6-2.7V12A10 10 0 0 0 12 2zm0 13a3 3 0 1 1 0-6 3 3 0 0 1 0 6z"/></svg>
        Wendell.Pask@kestrelforgetech.com
      </li>
      <li>
        <svg viewBox="0 0 24 24" aria-hidden="true"><path d="M12 2a10 10 0 1 0 0 20 10 10 0 0 0 0-20zm6.9 6h-2.8a15 15 0 0 0-1.3-3.6A8 8 0 0 1 18.9 8zM12 4a13 13 0 0 1 1.9 4h-3.8A13 13 0 0 1 12 4zM4.3 14a8 8 0 0 1 0-4h3.2a16 16 0 0 0 0 4zm.8 2h2.8a15 15 0 0 0 1.3 3.6A8 8 0 0 1 5.1 16zM7.9 8H5.1a8 8 0 0 1 4.1-3.6A15 15 0 0 0 7.9 8zM12 20a13 13 0 0 1-1.9-4h3.8A13 13 0 0 1 12 20zm2.3-6H9.7a14 14 0 0 1 0-4h4.6a14 14 0 0 1 0 4zm.5 5.6a15 15 0 0 0 1.3-3.6h2.8a8 8 0 0 1-4.1 3.6zm1.7-5.6a16 16 0 0 0 0-4h3.2a8 8 0 0 1 0 4z"/></svg>
        www.kestrelforgetech.com
      </li>
    </ul>
  </article>
</body>
</html>
```